Management consultant needs to update look of website

Currently I have a great word press website but it needs an updated look. I have new text for the site in the attached word document. I also have a list of websites whose design, look, and organization i like as a guide for the designer. The final design should be simple, strong, clear, and project the idea that my brand is a powerful authority in this space. Current site = www.brookfernadvisory.com

Target Market(s)

company owners / executives

Industry/Entity Type

Management Consulting

Number of Pages Required

3 page

Font styles to use
Serif

Colors

Designer to choose colors to be used in the design.

Requirements
Must have
• a simple and clear design and message. professional look. easy navigation. responsive to mobile devices. an easily implemented wordpress theme OR squarespace. use of my logo colors. though I am open to changing to a deep navy or charcoal logo image. source file uploaded.
Nice to have
• i like the cover photo and logo watermark on my current homepage. i like the google map with my logo on the current contact page. i like the animation as well. a great blend of the current site and something that is more seamless.

```html
<!DOCTYPE html>
<html lang="en">
<head>
<meta charset="utf-8">
<title>Brookfern Advisory — Home</title>
<link href="https://fonts.googleapis.com/css2?family=Cinzel:wght@400;600;700&family=Lato:wght@400;700&display=swap" rel="stylesheet">
<style>
:root{
  --gold:#cfad4c;
  --gold-deep:#a8893a;
  --gold-text:#c9a63f;
  --ink:#1b1b1b;
  --ink-deep:#0f0f0f;
  --white:#ffffff;
  --grey-text:#6f6f6f;
  --logo-grey:#bdbdbd;
  --frame-grey:#e4e4e4;
}
*{box-sizing:border-box;margin:0;padding:0}
html,body{width:1200px;height:3750px;overflow:hidden}
body{position:relative;background:var(--white);font-family:'Lato',Arial,sans-serif;color:var(--grey-text)}
.abs{position:absolute}

/* hero */
.hero{left:0;top:0;width:1200px;height:600px;background:linear-gradient(160deg,#5a5650 0%,#3a3835 45%,#25272b 100%)}
.hero-photo{left:0;top:0;width:1200px;height:600px;background:radial-gradient(ellipse at 50% 40%,rgba(120,115,105,.55),rgba(20,20,22,.6) 75%)}
.brand{left:78px;top:22px;display:flex;align-items:center;gap:12px}
.brand-mark{width:46px;height:46px;border-radius:50%;border:2px solid var(--gold)}
.brand-name{font-family:'Cinzel',Georgia,serif;font-size:17px;line-height:1.1;color:var(--gold);letter-spacing:1px}
.nav{right:80px;top:38px;display:flex;gap:28px;font-size:14px;font-weight:700;color:var(--white);letter-spacing:.5px}
.nav .active{border-bottom:2px solid var(--white);padding-bottom:5px}
.hero-title{left:0;top:190px;width:1200px;text-align:center;font-family:'Cinzel',Georgia,serif;font-weight:700;font-size:128px;line-height:130px;color:rgba(235,232,225,.88);letter-spacing:6px}

/* intro */
.intro-title{left:0;top:650px;width:1200px;text-align:center;font-family:'Cinzel',Georgia,serif;font-weight:700;font-size:35px;line-height:44px;color:var(--gold-text)}
.intro-text{left:320px;width:560px;text-align:center;font-size:14.5px;line-height:27px;color:var(--grey-text)}

/* gold band */
.gold-band{left:0;top:1100px;width:1200px;height:1525px;background:var(--gold)}
.desk-scene{left:130px;top:1000px;width:940px;height:340px;border-radius:8px;background:linear-gradient(180deg,rgba(240,240,240,.9) 0%,rgba(225,225,225,.55) 35%,rgba(230,220,190,.25) 100%)}
.section-title{left:0;width:1200px;text-align:center;font-family:'Cinzel',Georgia,serif;font-weight:700;color:var(--white)}
.testimonial{width:490px;height:200px;color:var(--white)}
.quote-badge{left:0;top:0;width:64px;height:64px;border-radius:50%;background:var(--white);color:var(--gold);font-family:'Cinzel',Georgia,serif;font-size:54px;font-weight:700;text-align:center;line-height:80px}
.t-name{left:90px;top:10px;font-size:15px;font-weight:700}
.t-role{left:90px;top:40px;font-size:13px}
.t-body{left:0;top:86px;width:490px;font-size:13.5px;line-height:26px}
.divider{height:1px;background:rgba(255,255,255,.3)}
.vdivider{left:599px;top:1480px;width:1px;height:1090px;border-left:1px dashed rgba(255,255,255,.3)}

/* client placeholders */
.logos-title{color:var(--gold-text);font-size:40px}
.client-logo{width:190px;height:80px;display:flex;align-items:center;gap:10px;font-weight:700;font-size:22px;line-height:22px;color:var(--logo-grey)}
.client-logo .sq{width:24px;height:24px;background:var(--logo-grey);flex:none}
.client-logo.featured{border:1px solid var(--frame-grey);box-shadow:0 2px 8px rgba(0,0,0,.06);color:var(--ink);padding-left:22px}
.client-logo.featured .sq{background:var(--ink)}

/* signup */
.signup{left:0;top:3092px;width:1200px;height:596px;background:var(--ink)}
.signup-title{color:var(--gold);font-size:33px;line-height:42px;top:3135px}
.signup-text{left:0;width:1200px;text-align:center;font-size:14px;line-height:27px;color:#e6e6e6}
.field{height:46px;border:1px solid var(--gold-deep);border-radius:3px;color:#ddd;font-size:14px;padding:14px}
.cta{left:325px;top:3380px;width:550px;height:46px;background:var(--gold-deep);border-radius:3px;text-align:center;font-family:'Cinzel',Georgia,serif;font-size:18px;line-height:46px;color:#1e1e1e;letter-spacing:1px}
.social{width:62px;height:62px;border-radius:50%;border:2px solid #cfcfcf}
.social::after{content:"";position:absolute;left:25px;top:25px;width:8px;height:8px;border-radius:50%;background:#e5e5e5}
.footer{left:0;top:3688px;width:1200px;height:62px;background:var(--ink-deep);text-align:center;font-size:13px;line-height:62px;color:#cfcfcf}
</style>
</head>
<body>

<header class="abs hero">
  <div class="abs hero-photo" role="img" aria-label="Photo of a team meeting in a bright open-plan office, darkened"></div>
  <div class="abs brand"><span class="brand-mark"></span><span class="brand-name">BROOKFERN<br>ADVISORY</span></div>
  <nav class="abs nav"><span class="active">HOME</span><span>ABOUT</span><span>SERVICES</span><span>ARTICLES</span><span>CONTACT</span></nav>
  <h1 class="abs hero-title">BROOKFERN<br>ADVISORY</h1>
</header>

<section>
  <h2 class="abs intro-title">GREAT COMPANIES SUCCEED BY<br>INVESTING IN THE RIGHT PEOPLE</h2>
  <p class="abs intro-text" style="top:752px">It's no secret that long-term business success requires a smart investment in the right people for your company. And yet, knowing how to cultivate a strong staff and keep them focused on the road ahead can be challenging for even the savviest organizational leaders and human resource executives.</p>
  <p class="abs intro-text" style="top:866px">I'm Dr. Miriam Castell and I want to help business owners, leaders, and HR teams understand how to identify, develop, and retain talented professionals who can take your success to the next level.</p>
</section>

<section>
  <div class="abs gold-band"></div>
  <div class="abs desk-scene" role="img" aria-label="Top-down desk scene with monitor showing colleagues, keyboard, mouse, phone, watch, pens, earphones and a small plant"></div>
  <h2 class="abs section-title" style="top:1390px;font-size:44px">TESTIMONIALS</h2>
  <div class="abs vdivider"></div>

  <div class="abs testimonial" style="left:80px;top:1475px"><div class="abs quote-badge">“</div><div class="abs t-name">-NAME SURNAME</div><div class="abs t-role">Lorem Ipsum is simply dummy.</div><p class="abs t-body">Lorem Ipsum is simply dummy text of the printing and typesetting industry. Lorem Ipsum has been the industry's standard dummy text ever since the 1500s, when an unknown printer took a galley of type and scrambled.</p></div>
  <div class="abs testimonial" style="left:625px;top:1475px"><div class="abs quote-badge">“</div><div class="abs t-name">-NAME SURNAME</div><div class="abs t-role">Lorem Ipsum is simply dummy.</div><p class="abs t-body">Lorem Ipsum is simply dummy text of the printing and typesetting industry. Lorem Ipsum has been the industry's standard dummy text ever since the 1500s, when an unknown printer took a galley of type and scrambled.</p></div>
  <div class="abs divider" style="left:80px;top:1662px;width:1040px"></div>

  <div class="abs testimonial" style="left:80px;top:1705px"><div class="abs quote-badge">“</div><div class="abs t-name">-NAME SURNAME</div><div class="abs t-role">Lorem Ipsum is simply dummy.</div><p class="abs t-body">Lorem Ipsum is simply dummy text of the printing and typesetting industry. Lorem Ipsum has been the industry's standard dummy text ever since the 1500s, when an unknown printer took a galley of type and scrambled.</p></div>
  <div class="abs testimonial" style="left:625px;top:1705px"><div class="abs quote-badge">“</div><div class="abs t-name">-NAME SURNAME</div><div class="abs t-role">Lorem Ipsum is simply dummy.</div><p class="abs t-body">Lorem Ipsum is simply dummy text of the printing and typesetting industry. Lorem Ipsum has been the industry's standard dummy text ever since the 1500s, when an unknown printer took a galley of type and scrambled.</p></div>
  <div class="abs divider" style="left:80px;top:1892px;width:1040px"></div>

  <div class="abs testimonial" style="left:80px;top:1935px"><div class="abs quote-badge">“</div><div class="abs t-name">-NAME SURNAME</div><div class="abs t-role">Lorem Ipsum is simply dummy.</div><p class="abs t-body">Lorem Ipsum is simply dummy text of the printing and typesetting industry. Lorem Ipsum has been the industry's standard dummy text ever since the 1500s, when an unknown printer took a galley of type and scrambled.</p></div>
  <div class="abs testimonial" style="left:625px;top:1935px"><div class="abs quote-badge">“</div><div class="abs t-name">-NAME SURNAME</div><div class="abs t-role">Lorem Ipsum is simply dummy.</div><p class="abs t-body">Lorem Ipsum is simply dummy text of the printing and typesetting industry. Lorem Ipsum has been the industry's standard dummy text ever since the 1500s, when an unknown printer took a galley of type and scrambled.</p></div>
  <div class="abs divider" style="left:80px;top:2122px;width:1040px"></div>

  <div class="abs testimonial" style="left:80px;top:2165px"><div class="abs quote-badge">“</div><div class="abs t-name">-NAME SURNAME</div><div class="abs t-role">Lorem Ipsum is simply dummy.</div><p class="abs t-body">Lorem Ipsum is simply dummy text of the printing and typesetting industry. Lorem Ipsum has been the industry's standard dummy text ever since the 1500s, when an unknown printer took a galley of type and scrambled.</p></div>
  <div class="abs testimonial" style="left:625px;top:2165px"><div class="abs quote-badge">“</div><div class="abs t-name">-NAME SURNAME</div><div class="abs t-role">Lorem Ipsum is simply dummy.</div><p class="abs t-body">Lorem Ipsum is simply dummy text of the printing and typesetting industry. Lorem Ipsum has been the industry's standard dummy text ever since the 1500s, when an unknown printer took a galley of type and scrambled.</p></div>
  <div class="abs divider" style="left:80px;top:2352px;width:1040px"></div>

  <div class="abs testimonial" style="left:80px;top:2395px"><div class="abs quote-badge">“</div><div class="abs t-name">-NAME SURNAME</div><div class="abs t-role">Lorem Ipsum is simply dummy.</div><p class="abs t-body">Lorem Ipsum is simply dummy text of the printing and typesetting industry. Lorem Ipsum has been the industry's standard dummy text ever since the 1500s, when an unknown printer took a galley of type and scrambled.</p></div>
  <div class="abs testimonial" style="left:625px;top:2395px"><div class="abs quote-badge">“</div><div class="abs t-name">-NAME SURNAME</div><div class="abs t-role">Lorem Ipsum is simply dummy.</div><p class="abs t-body">Lorem Ipsum is simply dummy text of the printing and typesetting industry. Lorem Ipsum has been the industry's standard dummy text ever since the 1500s, when an unknown printer took a galley of type and scrambled.</p></div>
</section>

<section>
  <h2 class="abs section-title logos-title" style="top:2670px">LOGOS</h2>
  <div class="abs client-logo" style="left:88px;top:2722px"><span class="sq"></span>company<br>name</div>
  <div class="abs client-logo" style="left:300px;top:2722px"><span class="sq"></span>company<br>name</div>
  <div class="abs client-logo" style="left:513px;top:2722px"><span class="sq"></span>company<br>name</div>
  <div class="abs client-logo" style="left:725px;top:2722px"><span class="sq"></span>company<br>name</div>
  <div class="abs client-logo" style="left:938px;top:2722px"><span class="sq"></span>company<br>name</div>
  <div class="abs client-logo" style="left:88px;top:2836px"><span class="sq"></span>company<br>name</div>
  <div class="abs client-logo" style="left:300px;top:2836px"><span class="sq"></span>company<br>name</div>
  <div class="abs client-logo" style="left:513px;top:2836px"><span class="sq"></span>company<br>name</div>
  <div class="abs client-logo featured" style="left:720px;top:2836px"><span class="sq"></span>company<br>name</div>
  <div class="abs client-logo" style="left:938px;top:2836px"><span class="sq"></span>company<br>name</div>
  <div class="abs client-logo" style="left:88px;top:2950px"><span class="sq"></span>company<br>name</div>
  <div class="abs client-logo" style="left:300px;top:2950px"><span class="sq"></span>company<br>name</div>
  <div class="abs client-logo" style="left:513px;top:2950px"><span class="sq"></span>company<br>name</div>
  <div class="abs client-logo" style="left:725px;top:2950px"><span class="sq"></span>company<br>name</div>
  <div class="abs client-logo" style="left:938px;top:2950px"><span class="sq"></span>company<br>name</div>
</section>

<section>
  <div class="abs signup"></div>
  <h2 class="abs section-title signup-title">LEARN TO INSPIRE EMPLOYEES AND<br>UNLOCK THEIR MAXIMUM POTENTIAL</h2>
  <p class="abs signup-text" style="top:3235px">If you're struggling to connect with today's employees and you need to develop a better<br>way to lead them, I want to help you become the very best leader possible.</p>
  <div class="abs field" style="left:325px;top:3325px;width:270px">Name</div>
  <div class="abs field" style="left:605px;top:3325px;width:270px">Email</div>
  <div class="abs cta">DOWNLOAD FREE INFORMATION</div>
  <p class="abs signup-text" style="top:3462px">You'll receive monthly updates filled with leader-focused resources and helpful information<br>that will help you build stronger organizational leaders. You can unsubscribe at any time.</p>
  <div class="abs social" style="left:494px;top:3552px" aria-label="Social link"></div>
  <div class="abs social" style="left:569px;top:3552px" aria-label="Social link"></div>
  <div class="abs social" style="left:644px;top:3552px" aria-label="Social link"></div>
</section>

<footer class="abs footer">2018 ©BROOKFERN ADVISORY · All Rights Reserved.</footer>

</body>
</html>
```